Business Card Design Project

We are a commercial talent casting company, a very "now" company. We need a new business card that is both current, graphic and elegantly interesting. As we are a service business,
we need something that will attract the attention of new clients,
yet project a business that is 25 years old.

Industry/Entity Type

Business

Requirements
Must have
• 1. Logo - Nora Quillan Casting
2. Address - 47 Thornbury Street
New York, New York 10010
3. Phone - 212-738-4192
4. E-Mail - Casting@noraquillan.example

Nice to have
• Would like the card in black and white with the only accent
color being red.

```html
<!DOCTYPE html>
<html lang="en">
<head>
<meta charset="utf-8">
<title>Nora Quillan Casting — Business Card</title>
<link rel="stylesheet" href="https://fonts.googleapis.com/css2?family=Old+Standard+TT:wght@400&family=Jost:wght@400&display=swap">
<style>
  :root {
    --backdrop: #e6e6e6;
    --card-white: #ffffff;
    --card-white-shade: #ececec;
    --ink: #111111;
    --card-black: #0c0708;
    --accent-red: #a8161b;
    --rule-dark: #2a2a2a;
    --text-light: #f2f2f2;
    --ornament-grey: #9a9a9a;
  }
  * { margin: 0; padding: 0; box-sizing: border-box; }
  html, body {
    width: 1200px;
    height: 808px;
    overflow: hidden;
    background: var(--backdrop);
  }
  .card {
    position: absolute;
    left: 50px;
    top: 92px;
    width: 1100px;
    height: 624px;
    background: var(--card-black);
    overflow: hidden;
  }
  .card__header {
    position: absolute;
    left: 0; top: 0;
    width: 100%;
    height: 224px;
    background: linear-gradient(180deg, var(--card-white) 0%, var(--card-white) 60%, var(--card-white-shade) 100%);
  }
  .card__name {
    position: absolute;
    left: 0; top: 34px;
    width: 100%;
    padding-left: 18px;
    text-align: center;
    font-family: "Old Standard TT", serif;
    font-size: 94px;
    line-height: 1;
    color: var(--ink);
  }
  .card__tagline {
    position: absolute;
    left: 0; top: 152px;
    width: 100%;
    padding-left: 22px;
    text-align: center;
    font-family: "Jost", sans-serif;
    font-size: 36px;
    letter-spacing: 0.2em;
    line-height: 1;
    color: var(--ink);
  }
  .card__rule {
    position: absolute;
    left: 0; top: 224px;
    width: 100%;
    height: 4px;
    background: var(--rule-dark);
  }
  .card__band {
    position: absolute;
    left: 0; top: 228px;
    width: 100%;
    height: 26px;
    background: var(--accent-red);
  }
  .card__gap {
    position: absolute;
    left: 0; top: 254px;
    width: 100%;
    height: 14px;
    background: var(--card-white);
  }
  .card__ornament {
    position: absolute;
    left: 0; top: 280px;
    width: 455px;
    height: 344px;
    background: radial-gradient(ellipse at 35% 60%, rgba(154,154,154,0.55) 0%, rgba(154,154,154,0.25) 45%, rgba(12,7,8,0) 75%);
  }
  .card__contact {
    position: absolute;
    right: 59px;
    top: 318px;
    text-align: right;
    font-family: "Jost", sans-serif;
    color: var(--text-light);
  }
  .contact__address {
    font-size: 33px;
    line-height: 58px;
    letter-spacing: 0.01em;
    text-transform: uppercase;
  }
  .contact__phone {
    margin-top: 26px;
    font-size: 58px;
    line-height: 1;
  }
  .contact__email {
    margin-top: 14px;
    font-size: 33px;
    line-height: 1;
    text-transform: uppercase;
  }
</style>
</head>
<body>
  <div class="card">
    <header class="card__header">
      <div class="card__name">Nora Quillan</div>
      <div class="card__tagline">CASTING</div>
    </header>
    <div class="card__rule"></div>
    <div class="card__band"></div>
    <div class="card__gap"></div>
    <div class="card__ornament" role="img" aria-label="Grey floral swirl ornament with leaves and curling vines"></div>
    <div class="card__contact">
      <div class="contact__address">47 Thornbury Street<br>New York, New York 10010</div>
      <div class="contact__phone">212-738-4192</div>
      <div class="contact__email">Casting@noraquillan.example</div>
    </div>
  </div>
</body>
</html>
```